Introducting Corbin Sheetmetal MADE WITH PRIDE

We require a PDF fact sheet that we can share via email that has a summary of infomation, services and products as found on our website www.corbinsheetmetal.example

The Call to Action - Heading should be "Made with Pride"

Needs to look professional, prefer sharp lines than bubble circles

Trying to attract new business

Target Market(s)

Potential new clients; Plumbers, Shop fitters, restaurants and Caters.

Industry/Entity Type

Manufacturing

Font styles to use
Other font styles liked:
• something masculine

Colors

Designer to choose colors to be used in the design.

Requirements
Must have
• Must be one page, low res so when emailing it's not too large.
• Must have phone number, email address and actual address
• Should include summary of copy from the website; www.corbinsheetmetal.example
• * A bit about us
• * Services
• * Fabrication Range and Finishes
• * General Fabrication
Nice to have
• Something that is not too busy, easy to read - so not too much writing. Must look professional (that's why we using ArtHive).
• Please let me know I you need images from the website and I'll sent to you.
Should not have
• It shouldn't be too busy, easy to read - so not too much writing. Simple and clear message.

```html
<!DOCTYPE html>
<html lang="en">
<head>
<meta charset="utf-8">
<title>Corbin Sheetmetal – Made With Pride</title>
<link rel="stylesheet" href="https://fonts.googleapis.com/css2?family=Oswald:wght@500;600&family=Roboto+Condensed:wght@400;700&display=swap">
<style>
  :root {
    --page-bg: #e9e8e6;
    --sheet-dark: #252427;
    --header-grey: #c9cbcc;
    --panel-slate: #3c4957;
    --text-light: #ffffff;
    --text-dark: #2f3b47;
    --photo-steel: #8a8c8f;
    --photo-machine: #3a63a8;
    --photo-welder: #8a6a4c;
  }
  * { box-sizing: border-box; margin: 0; padding: 0; }
  html, body { width: 1200px; height: 966px; overflow: hidden; background: var(--page-bg); }
  .flyer {
    position: absolute; left: 271px; top: 18px;
    width: 658px; height: 930px;
    background: var(--sheet-dark);
    color: var(--text-light);
    font-family: "Roboto Condensed", Arial, sans-serif;
    overflow: hidden;
  }
  .header-band {
    position: absolute; left: 300px; top: 0; width: 358px; height: 180px;
    background: var(--header-grey);
    display: flex; align-items: center; justify-content: center; gap: 12px;
  }
  .brand-mark { width: 26px; height: 26px; background: var(--text-dark); }
  .brand-name {
    font-family: "Roboto Condensed", Arial, sans-serif; font-weight: 700;
    font-size: 24px; letter-spacing: 1px; text-transform: uppercase; color: var(--text-dark);
  }
  .photo-collage { position: absolute; left: 0; top: 0; }
  .intro {
    position: absolute; left: 360px; top: 205px; width: 275px;
    font-size: 14px; line-height: 1.4; text-align: justify;
  }
  .headline {
    position: absolute; left: 0; right: 0; top: 395px; text-align: center;
    font-family: "Oswald", Impact, sans-serif; font-weight: 600;
    font-size: 84px; letter-spacing: 0.5px; line-height: 1; text-transform: uppercase;
  }
  .columns {
    position: absolute; left: 34px; top: 520px; width: 590px; height: 290px;
    display: grid; grid-template-columns: repeat(3, 1fr); gap: 10px;
  }
  .column { background: var(--panel-slate); padding: 18px 16px; }
  .column h2 {
    font-family: "Oswald", Impact, sans-serif; font-weight: 500;
    font-size: 22px; line-height: 1.05; text-transform: uppercase; text-align: center; margin-bottom: 8px;
  }
  .column p { font-size: 15px; line-height: 1.3; }
  .contact { position: absolute; left: 0; right: 0; top: 832px; text-align: center; }
  .contact .address { font-size: 25px; }
  .contact .reach { font-size: 17px; font-weight: 700; margin-top: 6px; }
</style>
</head>
<body>
<article class="flyer">
  <svg class="photo-collage" width="300" height="360" viewBox="0 0 300 360">
    <defs>
      <clipPath id="coil-clip"><circle cx="140" cy="110" r="118"/></clipPath>
      <clipPath id="welder-clip"><circle cx="230" cy="265" r="100"/></clipPath>
    </defs>
    <rect x="0" y="80" width="190" height="270" fill="var(--photo-machine)" role="img" aria-label="Photo of blue metal folding machinery"/>
    <circle cx="140" cy="110" r="122" fill="#fff"/>
    <rect x="0" y="0" width="300" height="240" fill="var(--photo-steel)" clip-path="url(#coil-clip)" role="img" aria-label="Photo of stacked rolls of sheet steel"/>
    <circle cx="230" cy="265" r="106" fill="#fff"/>
    <rect x="120" y="160" width="220" height="220" fill="var(--photo-welder)" clip-path="url(#welder-clip)" role="img" aria-label="Photo of a tradesperson welding in a hi-vis vest"/>
  </svg>

  <header class="header-band">
    <span class="brand-mark"></span>
    <span class="brand-name">Corbin Sheetmetal</span>
  </header>

  <p class="intro">Fast, friendly, and fully functional, our professional Metal Fabrication Service. We provide general sheetmetal and light steel fabrication services (cutting, folding, mig/tig welding) working with stainless steel, copper, galvanised steel, aluminium and mild steel.</p>

  <h1 class="headline">Made With Pride</h1>

  <section class="columns">
    <div class="column">
      <h2>Services</h2>
      <p>We can produce and supply a range of sheet metal components for all industries. We provide general sheetmetal and light steel fabrication services (cutting, folding, mig/tig welding) working with stainless steel, aluminium, copper, galvanised steel and mild steel.</p>
    </div>
    <div class="column">
      <h2>Facilities, Materials &amp; Finishes</h2>
      <p>We have an extensive range of equipment &amp; sheet metal machinery. We have experienced tradespeople with extensive experience &amp; abilities to custom fabricate to your specific design. Contact us now</p>
    </div>
    <div class="column">
      <h2>General Fabrication</h2>
      <p>Whether you're performing shop fabrication, repairing equipment on a farm or job site, or creating artwork in your garage, Corbin Sheetmetal has the knowhow, creativity and process knowledge to help you get your job done right.</p>
    </div>
  </section>

  <footer class="contact">
    <p class="address">48 Harlow St, Millbrook SA 5999, Australia</p>
    <p class="reach">(08) 5550 1234 | info@corbinsheetmetal.example | www.corbinsheetmetal.example</p>
  </footer>
</article>
</body>
</html>
```